GravaLoop. Customer needs to know about us, what services we provide & contact us

We are a waste tire recycling company. Our primary focus is on providing a sustainable and cost effective service focusing on: Waste Tire Management, Hassle Free Scheduling for Tire Collection, Mobile Shredding & Special site cleanup services. GravaLoop will be producing TDF, Clean Tire Wire & further materials.
Please look at https://harvonrubber.example
Please look at https://quelbamaterials.example

This is the look and feel of what we want

I have attached a word document with our website info.

Target Market(s)

Tire Install Companies. Such as morbanhaul.example. TDF Purchasers such as pelkofuel.example.

Industry/Entity Type

Waste Tire Recycling

Coding

Coded - Design and coding required

Number of Pages Required

3 page

Font styles to use
Other font styles liked:
• Look at our logo

Requirements
Must have
• We need a 3 page setup for About Us, Services & Contact Us. Contact us should be a form them can fill out and submit to us Images that are related to waste tire recycling. Clean, modern, innovative.
Nice to have
• The color and feel of the website should work with our logo that we did with artpivot
Should not have
• Anything progressive, political or "woke"

```html
<!DOCTYPE html>
<html lang="en">
<head>
<meta charset="utf-8">
<title>GravaLoop – Waste Tire Recycling</title>
<link href="https://fonts.googleapis.com/css2?family=Teko:wght@400;500;600&family=Poppins:wght@400;500;600&display=swap" rel="stylesheet">
<style>
:root{
  --green:#169845;
  --green-dark:#0f7a36;
  --green-pale:#d9eddf;
  --ink:#1d1d1d;
  --text:#3a3a3a;
  --line:#d6d6d6;
  --card-border:#e3e3e3;
  --footer:#050505;
  --footer-bar:#2a2a2a;
  --white:#ffffff;
}
*{box-sizing:border-box;margin:0;padding:0}
html,body{width:1200px;height:3647px;overflow:hidden}
body{position:relative;background:var(--white);font-family:'Poppins',sans-serif;color:var(--text)}
.abs{position:absolute}
.heading{font-family:'Teko',sans-serif;font-weight:500;letter-spacing:1px;color:var(--ink);text-transform:uppercase;line-height:1}
.btn{position:absolute;display:flex;align-items:center;justify-content:center;background:var(--green);color:var(--white);font-family:'Teko',sans-serif;font-weight:500;font-size:19px;letter-spacing:1px;text-transform:uppercase;padding-top:3px}

/* header */
.site-header{position:absolute;left:0;top:0;width:1200px;height:67px;background:var(--white)}
.brand{position:absolute;display:flex;align-items:center;gap:8px;font-family:'Poppins',sans-serif;font-weight:600;color:var(--green)}
.brand-dot{width:14px;height:14px;border-radius:50%;background:var(--green)}
.main-nav{position:absolute;top:24px;left:767px;display:flex;gap:28px;font-size:14px;font-weight:500;color:#333}

/* hero */
.hero{position:absolute;left:0;top:67px;width:1200px;height:547px;background:linear-gradient(90deg,#2b2b28 0%,#3d3b35 45%,#565249 70%,#3a3833 100%)}
.hero-title{position:absolute;left:156px;top:100px;font-family:'Teko',sans-serif;font-weight:500;font-size:100px;line-height:88px;color:var(--white);letter-spacing:3px}
.hero-title span{color:var(--green)}
.hero-copy{position:absolute;left:156px;top:286px;width:420px;font-size:16.5px;line-height:24px;color:var(--white)}

/* services */
.services-photo{position:absolute;left:156px;top:726px;width:394px;height:449px;background:linear-gradient(160deg,#4f5a3a 0%,#2d2d2b 55%,#1f1f1f 100%)}
.services-label{position:absolute;left:156px;top:990px;width:394px;text-align:center;color:var(--white);font-size:46px}
.services-rule{position:absolute;left:303px;top:1053px;width:100px;height:3px;background:var(--white)}
.card{position:absolute;width:222px;height:211px;border:1px solid var(--card-border);background:var(--white);text-align:center}
.card-icon{width:38px;height:38px;margin:26px auto 22px;background:var(--green);border-radius:6px}
.card h3{font-family:'Teko',sans-serif;font-weight:500;font-size:20px;line-height:24px;letter-spacing:1px;color:var(--ink);text-transform:uppercase}
.card hr{width:38px;border:0;height:2px;background:var(--green);margin:8px auto 10px}
.card p{font-size:11.5px;line-height:19px;padding:0 16px;color:#444}

/* who we are */
.who-frame{position:absolute;left:156px;top:1257px;width:887px;height:414px;background:var(--green)}
.who-inner{position:absolute;left:173px;top:1272px;width:853px;height:416px;background:var(--green-pale)}
.who-card{position:absolute;left:190px;top:1288px;width:819px;height:417px;background:var(--white);box-shadow:0 6px 14px rgba(0,0,0,.08);text-align:center}
.who-card .heading{font-size:46px;margin-top:76px}
.rule-green{width:58px;height:3px;background:var(--green);margin:12px auto 26px}
.who-card p{font-size:13px;line-height:24px;padding:0 100px;color:#333}

/* experience */
.years{position:absolute;left:0;top:1760px;width:1200px;text-align:center;font-family:'Teko',sans-serif;font-weight:600;font-size:200px;line-height:170px;letter-spacing:12px;color:#1f2428}
.exp-line{position:absolute;top:1973px;height:2px;background:var(--line)}
.exp-label{position:absolute;left:0;top:1950px;width:1200px;text-align:center;font-size:46px}

/* produce */
.produce-title{position:absolute;left:156px;top:2183px;font-size:46px}
.produce-sub{position:absolute;left:156px;top:2253px;font-family:'Teko',sans-serif;font-weight:500;font-size:28px;color:var(--green);letter-spacing:1px}
.produce-rule{position:absolute;left:156px;top:2294px;width:419px;height:2px;background:var(--green)}
.produce-copy{position:absolute;left:156px;top:2321px;width:422px;font-size:13px;line-height:24px;color:#333}
.produce-photo{position:absolute;left:648px;top:2189px;width:395px;height:420px;background:linear-gradient(170deg,#8a9097 0%,#4b4d50 40%,#2a2b2c 100%)}

/* contact */
.contact{position:absolute;left:0;top:2690px;width:1200px;height:550px;background:linear-gradient(180deg,#1a9b48 0%,#15903f 100%)}
.contact .heading{position:absolute;left:0;top:78px;width:1200px;text-align:center;color:var(--white);font-size:46px}
.contact-sub{position:absolute;left:0;top:137px;width:1200px;text-align:center;font-size:13px;color:var(--white)}
.field{position:absolute;border:1px solid rgba(255,255,255,.7);color:var(--white);font-size:13px;padding:14px 16px}
.btn-light{background:var(--white);color:var(--green)}

/* footer */
.site-footer{position:absolute;left:0;top:3240px;width:1200px;height:344px;background:var(--footer);color:var(--white)}
.footer-about{position:absolute;left:156px;top:156px;width:330px;font-size:13px;line-height:24px}
.footer-title{position:absolute;font-family:'Teko',sans-serif;font-weight:500;font-size:32px;color:var(--green);letter-spacing:1px;text-transform:uppercase}
.footer-links{position:absolute;left:588px;top:150px;list-style:none;font-size:13px;line-height:24px}
.contact-row{position:absolute;left:798px;display:flex;font-size:13px;line-height:24px}
.contact-row dt{width:70px;font-family:'Teko',sans-serif;font-weight:500;font-size:16px;letter-spacing:1px}
.contact-row dd{width:190px}
.footer-bar{position:absolute;left:0;top:3584px;width:1200px;height:63px;background:var(--footer-bar);color:var(--white);font-size:13px;display:flex;align-items:center;justify-content:center}
</style>
</head>
<body>

<header class="site-header">
  <div class="brand" style="left:54px;top:18px;font-size:22px"><span class="brand-dot"></span>GravaLoop</div>
  <nav class="main-nav"><span>About Us</span><span>Service</span><span>Contact Us</span></nav>
  <svg class="abs" style="left:1077px;top:25px" width="18" height="18" viewBox="0 0 18 18" fill="none" stroke="#333" stroke-width="1.8"><circle cx="7.5" cy="7.5" r="6"/><line x1="12" y1="12" x2="17" y2="17"/></svg>
  <svg class="abs" style="left:1119px;top:23px" width="28" height="20" viewBox="0 0 28 20" stroke="#333" stroke-width="2"><line x1="0" y1="2" x2="28" y2="2"/><line x1="8" y1="10" x2="28" y2="10"/><line x1="4" y1="18" x2="28" y2="18"/></svg>
</header>

<section class="hero" role="img" aria-label="Piles of shredded rubber and stacked used tires at a recycling yard">
  <h1 class="hero-title">WECOME TO<br><span>GRAVALOOP</span></h1>
  <p class="hero-copy">Lorem ipsum dolor sit amet, consectetur adipiscing elit, sed do eiusmod tempor incididunt ut labore et dolore magna aliqua.</p>
  <a class="btn" style="left:156px;top:386px;width:227px;height:47px">Start Recycling With Us</a>
</section>

<section aria-label="Our services">
  <div class="services-photo" role="img" aria-label="Worker in orange overalls sorting a large pile of used tires"></div>
  <h2 class="heading services-label">Our Services</h2>
  <div class="services-rule"></div>
  <a class="btn" style="left:260px;top:1080px;width:188px;height:47px">See Our Services</a>

  <div class="card" style="left:575px;top:726px"><div class="card-icon"></div><h3>Waste Tiremanagement<br>&amp; Recycling</h3><hr><p>Lorem ipsum dolor sit amet, consectetur adipiscing elit, sed</p></div>
  <div class="card" style="left:821px;top:726px"><div class="card-icon"></div><h3>Scheduling &amp; Billing</h3><hr><p>Lorem ipsum dolor sit amet, consectetur adipiscing elit, sed do eiusmod</p></div>
  <div class="card" style="left:575px;top:964px"><div class="card-icon"></div><h3>First Rate Customer<br>Support &amp; Service</h3><hr><p>Lorem ipsum dolor sit amet, consectetur adipiscing elit, sed</p></div>
  <div class="card" style="left:821px;top:964px"><div class="card-icon"></div><h3>Tire Remediation &amp;<br>Special Tire Clean-Ups</h3><hr><p>Lorem ipsum dolor sit amet, consectetur adipiscing elit, sed</p></div>
</section>

<section aria-label="Who we are">
  <div class="who-frame"></div>
  <div class="who-inner"></div>
  <div class="who-card">
    <h2 class="heading">Who We Are</h2>
    <div class="rule-green"></div>
    <p>Every Year The Federal Waste Board estimates that over 300 million scrap tires are generated annually. GravaLoop is your sustainable business partner that is leading the way forward with a more sustainable eco-friendly approach to the scarp tire industry. Properly reclaiming and recycling these tires into reusable raw materials protects the environment and public health.</p>
  </div>
  <a class="btn" style="left:507px;top:1576px;width:186px;height:48px">More About Us</a>
</section>

<section aria-label="Experience">
  <div class="years">20 YEARS</div>
  <div class="exp-line" style="left:156px;width:303px"></div>
  <div class="exp-line" style="left:741px;width:302px"></div>
  <h2 class="heading exp-label">Of Experience</h2>
  <a class="btn" style="left:507px;top:2036px;width:186px;height:48px">Make An Appoinment</a>
</section>

<section aria-label="What we produce">
  <h2 class="heading produce-title">What We Produce</h2>
  <div class="produce-sub">TDF</div>
  <div class="produce-rule"></div>
  <p class="produce-copy">GravaLoop seeks to be one of the leading TDF suppliers to the region. This is a product with a wide range of demand from pulp and paper mills, electrical utilities, industrial boilers to cement and asphalt plants our expertly handled tire-derived fuel is being used and receiving high marks for its ever-expanding list of benefits. From driving boiler efficiency to stamping out emissions, GravaLoop wants to be your TDF supplier offering additional services to include tire pick-up to TDF drop-off we have your back!</p>
  <a class="btn" style="left:156px;top:2562px;width:151px;height:47px">View Details</a>
  <div class="produce-photo" role="img" aria-label="Conveyor dropping a heap of shredded tire-derived fuel chips"></div>
</section>

<section class="contact" aria-label="Get in touch">
  <h2 class="heading">Get In Touch</h2>
  <p class="contact-sub">If you have any questions, just fill in the contact form, and we will be in contact shortly</p>
  <div class="field" style="left:156px;top:183px;width:287px;height:46px">Company Name:</div>
  <div class="field" style="left:456px;top:183px;width:287px;height:46px">Email Address:</div>
  <div class="field" style="left:757px;top:183px;width:286px;height:46px">Phone Number:</div>
  <div class="field" style="left:156px;top:240px;width:287px;height:46px">Address of Business for PickUp:</div>
  <div class="field" style="left:456px;top:240px;width:287px;height:46px">Number of tires:</div>
  <div class="field" style="left:757px;top:240px;width:286px;height:46px">Pickup Frequency:</div>
  <div class="field" style="left:156px;top:298px;width:887px;height:91px">Type Your Message:</div>
  <a class="btn btn-light" style="left:524px;top:423px;width:151px;height:47px">Send Message</a>
</section>

<footer class="site-footer">
  <div class="brand" style="left:156px;top:100px;font-size:26px"><span class="brand-dot"></span>GravaLoop</div>
  <p class="footer-about">We are an industry-leading and award-winning construction services provider ready to work on a project of any complexity, whether it's commercial or residential.</p>
  <h3 class="footer-title" style="left:587px;top:96px">Quick Links</h3>
  <ul class="footer-links"><li>About Us</li><li>service</li><li>contact us</li></ul>
  <h3 class="footer-title" style="left:798px;top:96px">Contact Us</h3>
  <dl>
    <div class="contact-row" style="top:146px"><dt>LOCATION</dt><dd>1182 Marlow Ridge Rd, Calderon, CA 90415</dd></div>
    <div class="contact-row" style="top:208px"><dt>PHONE</dt><dd>+1 555-014-2290</dd></div>
    <div class="contact-row" style="top:248px"><dt>E-MAIL</dt><dd>info@gravaloop.example</dd></div>
  </dl>
</footer>
<div class="footer-bar">© 2022 GravaLoop | All rights reserved | Privacy Policy</div>

</body>
</html>
```